Zielgruppe
Hausarztpraxis Dr. Wildhagen
Patientenbetreuung / Junge Patienten
Aufgabenstellung
Bitte Mit dem Praxis Logo. Gern auch ein Foto aus der Praxis. In den Farben der Praxis Weiß-Magenta-Grau
Es soll kein Newsletter an sich werden, sondern eine Email die die Patienten nach Ihrem Besuch in der Praxis bekommen. Dort soll dann die Suchflixseite verlinkt sein mit einem Button zum bewerten!

```html
<!DOCTYPE html>
<html lang="de">
<head>
<meta charset="utf-8">
<title>Hausarztpraxis Dr. Wildhagen – Ihre Meinung ist uns wichtig</title>
<link rel="stylesheet" href="https://fonts.googleapis.com/css2?family=Open+Sans:wght@400;600;700&display=swap">
<style>
  :root {
    --magenta: #c41a56;
    --magenta-soft: #cf4677;
    --magenta-overlay: rgba(188, 28, 90, 0.82);
    --pink: #f26ba0;
    --grey-text: #5a5a5a;
    --grey-mark: #595d62;
    --white: #ffffff;
  }
  * { box-sizing: border-box; margin: 0; padding: 0; }
  html, body { width: 1047px; height: 1200px; overflow: hidden; background: var(--white); }
  body { font-family: "Open Sans", sans-serif; color: var(--grey-text); position: relative; }

  .brand { position: absolute; top: 20px; left: 0; width: 1047px; text-align: center; }
  .brand-ring { display: block; margin: 0 auto; }
  .brand-name { margin-top: 12px; font-size: 15px; font-weight: 600; color: var(--magenta); letter-spacing: 0.5px; }

  .hero-photo {
    position: absolute; top: 159px; left: 0; width: 1047px; height: 292px;
    background: linear-gradient(100deg, #e9e7e5 0%, #f3f2f0 35%, #b7afa3 60%, #d2d0ce 78%, #8e8c8e 100%);
  }

  .headline-box {
    position: absolute; top: 375px; left: 227px; width: 593px; height: 132px;
    background: linear-gradient(to bottom, var(--magenta-overlay) 0, var(--magenta-overlay) 76px, var(--magenta-soft) 76px);
    color: var(--white); text-align: center;
  }
  .headline-box h1 { font-weight: 400; font-size: 29px; margin-top: 31px; line-height: 1.2; }
  .headline-box p { font-size: 13px; margin-top: 9px; }

  .message { position: absolute; top: 564px; left: 227px; width: 593px; text-align: center; font-size: 13px; line-height: 17.5px; }
  .message p + p { margin-top: 17.5px; }
  .phone { color: var(--magenta); font-weight: 700; }

  .rate-button {
    display: block; width: 216px; height: 36px; margin: 21px auto 22px;
    border-radius: 18px; background: var(--magenta); color: var(--white);
    font-size: 13px; line-height: 36px; text-decoration: underline;
  }

  .info-row { position: absolute; top: 976px; left: 227px; width: 593px; display: flex; gap: 8px; }
  .info-box { flex: 1; height: 127px; color: var(--white); font-size: 10px; line-height: 14px; padding: 10px 20px 0 23px; }
  .info-box h2 { font-size: 11px; font-weight: 700; margin-bottom: 14px; }
  .info-box p + p { margin-top: 14px; }
  .info-box--hours { background: var(--pink); }
  .info-box--phone { background: var(--magenta); padding-left: 20px; }

  .footer-band { position: absolute; top: 1160px; left: 0; width: 1047px; height: 10px; background: var(--pink); }
  .footer { position: absolute; top: 1170px; left: 0; width: 1047px; height: 30px; background: var(--magenta); color: var(--white); text-align: center; font-size: 12px; line-height: 28px; }
</style>
</head>
<body>
  <header class="brand">
    <svg class="brand-ring" width="56" height="56" viewBox="0 0 56 56" aria-hidden="true">
      <circle cx="28" cy="28" r="25" fill="none" stroke="var(--magenta)" stroke-width="3"/>
    </svg>
    <div class="brand-name">Hausarztpraxis Dr. med. Wendela Wildhagen</div>
  </header>

  <div class="hero-photo" role="img" aria-label="Foto des hellen Wartebereichs der Praxis mit weißen Stühlen, Bambusstäben und grauen Sesseln"></div>

  <section class="headline-box">
    <h1>Ihre Meinung ist uns wichtig.</h1>
    <p>Nehmen Sie sich kurz zeit und bewerten Sie uns auf Suchflix.</p>
  </section>

  <main class="message">
    <p>Liebe Patientin, Lieber Patient,</p>
    <p>wie war Ihre Erfahrung in unserer Praxis?</p>
    <p>Wir versuchen uns ständig zu verbessern und freuen uns, wenn Sie uns ein kurzes Feedback geben würden. Es Wäre toll, wenn Sie sich kurz die Zeit nehmen um eine Bewertung bei Suchflix zu schreiben, denn damit hilfst du uns und auch anderen Patienten uns zu finden.</p>
    <p>Um Ihre Bewertung zu schreiben und abzuschicken genügt ein Klick!</p>
    <a class="rate-button" href="#">Hier bewerten</a>
    <p>Vielen Dank im Voraus für Ihre Bewertung!<br>Bei Fragen oder falls Sie uns erneut besuchen möchten, stehen wir Ihnen gern jederzeit zur Verfügung!</p>
    <p>Melden Sie sich gern unter der <span class="phone">01234 - 5678</span> oder wieder über unseren Online Terminkalender der Website.</p>
  </main>

  <section class="info-row">
    <div class="info-box info-box--hours">
      <h2>Sprechzeiten:</h2>
      <p>Montag: 8:00-11:30 und 14:00-17:00 Uhr<br>Dienstag: 8:00-13:00 Uhr<br>Mittwoch: 8:00-13:00 Uhr<br>Donnerstag: 8:00-11:30 und 14:00-18:00 Uhr<br>Freitag: 8:00-11:30 Uhr</p>
    </div>
    <div class="info-box info-box--phone">
      <h2>Telefonische Erreichbarkeit:</h2>
      <p>tägl. von 8:30-11:00 Uhr sowie Montag und Donnerstag von 14:00- 16:00 Uhr.</p>
      <p>Wir bitte um vorherige Terminvereinbarung telefonisch oder über unseren Onlinekalender.</p>
    </div>
  </section>

  <div class="footer-band"></div>
  <footer class="footer">Impressum &nbsp;I Datenschutz I Unsere Praxis I Kontakt</footer>
</body>
</html>
```